Veltra - Medical Device Company Needs Box Refined

We are a medical device company needing our packaging refined. This she be clean and sophisticated. The logo must not be change. Please see the attached sample for baseline and sizing.

Industry/Entity Type

It Company

```html
<!DOCTYPE html>
<html lang="en">
<head>
<meta charset="utf-8">
<title>Veltra – Hydrophilic Acrylic Intraocular Lens Packaging</title>
<link rel="stylesheet" href="https://fonts.googleapis.com/css2?family=Arimo:wght@400;700&display=swap">
<style>
  :root {
    --stage: #d9dadc;
    --panel-white: #ffffff;
    --panel-mist: #e8f2fa;
    --panel-sky: #d2e5f3;
    --side-tint: #eef2f7;
    --brand-blue: #1f5ea8;
    --brand-navy: #15468a;
    --brand-yellow: #f2d21b;
    --headline-grey: #8a8f96;
    --symbol-grey: #4a4f57;
    --band-text: #ffffff;
  }
  html, body {
    margin: 0;
    padding: 0;
    width: 1200px;
    height: 948px;
    overflow: hidden;
    background: var(--stage);
    font-family: "Arimo", Arial, sans-serif;
  }
  .canvas {
    position: relative;
    width: 1200px;
    height: 948px;
  }
  .box-front {
    position: absolute;
    left: 60px;
    top: 180px;
    width: 900px;
    height: 590px;
    background: var(--panel-white);
    overflow: hidden;
    box-shadow: 0 18px 40px rgba(0, 0, 0, 0.16);
  }
  .panel-backdrop {
    position: absolute;
    inset: 0;
    width: 100%;
    height: 100%;
  }
  .brand-mark {
    position: absolute;
    left: 34px;
    top: 62px;
    display: flex;
    align-items: center;
    gap: 10px;
  }
  .brand-mark__dot {
    width: 18px;
    height: 18px;
    border-radius: 50%;
    background: var(--brand-yellow);
  }
  .brand-mark__name {
    font-size: 44px;
    font-weight: 400;
    color: var(--brand-blue);
  }
  .product-title {
    position: absolute;
    left: 216px;
    top: 44px;
    margin: 0;
    font-size: 26px;
    font-weight: 400;
    letter-spacing: 0.8px;
    color: var(--headline-grey);
    white-space: nowrap;
  }
  .eye-artwork {
    position: absolute;
    left: 220px;
    top: 78px;
    width: 610px;
    height: 420px;
    border-radius: 50%;
    background: radial-gradient(ellipse at 50% 50%,
      var(--brand-navy) 0%,
      var(--brand-blue) 32%,
      rgba(31, 94, 168, 0.55) 60%,
      rgba(31, 94, 168, 0.15) 82%,
      rgba(31, 94, 168, 0) 100%);
  }
  .contents-band {
    position: absolute;
    left: 0;
    bottom: 0;
    width: 100%;
    height: 98px;
    background: var(--brand-blue);
  }
  .contents-band__texture {
    position: absolute;
    right: 0;
    top: 0;
    width: 320px;
    height: 100%;
    background: linear-gradient(100deg, rgba(255,255,255,0) 0%, rgba(255,255,255,0.2) 70%, rgba(255,255,255,0.3) 100%);
  }
  .contents-band__label {
    position: absolute;
    left: 24px;
    top: 16px;
    margin: 0;
    font-size: 13px;
    letter-spacing: 0.4px;
    color: var(--band-text);
  }
  .contents-band__item {
    position: absolute;
    left: 24px;
    top: 36px;
    margin: 0;
    font-size: 21px;
    font-weight: 700;
    letter-spacing: 1.2px;
    color: var(--band-text);
  }
  .box-side {
    position: absolute;
    left: 960px;
    top: 180px;
    width: 170px;
    height: 590px;
    background: linear-gradient(180deg, var(--panel-white) 0%, var(--side-tint) 100%);
    box-shadow: 0 18px 40px rgba(0, 0, 0, 0.16);
    border-left: 1px solid #c9d2dc;
    overflow: hidden;
  }
  .side-symbols {
    position: absolute;
    left: 0;
    top: 0;
    width: 170px;
    height: 460px;
  }
  .side-symbols text {
    font-family: "Arimo", Arial, sans-serif;
    fill: var(--symbol-grey);
  }
  .side-brand {
    position: absolute;
    left: 85px;
    top: 520px;
    transform: translate(-50%, -50%) rotate(-90deg);
    display: flex;
    align-items: center;
    gap: 8px;
    white-space: nowrap;
  }
  .side-brand__dot {
    width: 12px;
    height: 12px;
    border-radius: 50%;
    background: var(--brand-yellow);
  }
  .side-brand__name {
    font-size: 30px;
    color: var(--brand-blue);
  }
</style>
</head>
<body>
<main class="canvas">
  <section class="box-front">
    <svg class="panel-backdrop" viewBox="0 0 900 590" preserveAspectRatio="none" aria-hidden="true">
      <defs>
        <linearGradient id="panel-wash" x1="0" y1="0" x2="0" y2="1">
          <stop offset="0" stop-color="var(--panel-mist)"/>
          <stop offset="1" stop-color="var(--panel-sky)"/>
        </linearGradient>
      </defs>
      <path d="M0 250 C 230 170, 540 130, 900 150 L 900 590 L 0 590 Z" fill="url(#panel-wash)"/>
      <path d="M0 250 C 230 170, 540 130, 900 150" fill="none" stroke="#ffffff" stroke-width="3" opacity="0.8"/>
    </svg>

    <div class="brand-mark">
      <span class="brand-mark__dot"></span>
      <span class="brand-mark__name">Veltra</span>
    </div>

    <h1 class="product-title">HYDROPHILIC ACRYLIC INTRAOCULAR LENS</h1>

    <div class="eye-artwork" role="img" aria-label="Large blue halftone illustration of a human eye"></div>

    <div class="contents-band">
      <div class="contents-band__texture" role="img" aria-label="Blue halftone dot texture"></div>
      <p class="contents-band__label">CONTENTS:</p>
      <p class="contents-band__item">ONE INTRAOCULAR LENS</p>
    </div>
  </section>

  <aside class="box-side">
    <svg class="side-symbols" viewBox="0 0 170 460" aria-label="Handling symbols">
      <g stroke="var(--symbol-grey)" stroke-width="2" fill="none">
        <!-- single use -->
        <circle cx="85" cy="96" r="13"/>
        <line x1="76" y1="87" x2="94" y2="105"/>
        <line x1="94" y1="87" x2="76" y2="105"/>
        <!-- do not resterilize -->
        <circle cx="85" cy="178" r="13"/>
        <line x1="76" y1="169" x2="94" y2="187"/>
        <!-- keep dry / package -->
        <circle cx="85" cy="258" r="13"/>
        <circle cx="85" cy="258" r="6"/>
        <!-- caution -->
        <path d="M85 326 L100 352 L70 352 Z"/>
        <line x1="85" y1="334" x2="85" y2="344"/>
        <!-- sterile -->
        <rect x="74" y="388" width="22" height="58"/>
      </g>
      <text transform="translate(92 78) rotate(-90)" font-size="10" font-weight="700">Single</text>
      <text transform="translate(104 78) rotate(-90)" font-size="10" font-weight="700">Use Only</text>
      <text transform="translate(89 442) rotate(-90)" font-size="10" font-weight="700">STERILE</text>
    </svg>

    <div class="side-brand">
      <span class="side-brand__dot"></span>
      <span class="side-brand__name">Veltra</span>
    </div>
  </aside>
</main>
</body>
</html>
```